Wine Label for a Prosecco Wine Called Vuro

Prosecco is a white sparkling wine from Italy. We are looking for an eye catching, elegant label for this prosecco that is called "Vuro" because it is a young, fresh, lively white sparkling wine. (We do not want to see children or babies featured on the label-- just the name VURO please.) Attached is the old label for your reference, and the bottle type that will be used , which is a dark green Burgundy style bottle (pls ignore the label on the bottle). Please no grapes or wine glasses on the label. We are looking for something: eye catching / fun / ELEGANT (not cheap). We would be happy with a fun color too. Remember-- elegant, eye catching! Thanks!
Updates

Hi All, I think I made a mistake in my brief and have updated it. I also uploaded a competitor's label that we like very much to give better direction to what we are looking for. Also, the word Vuro cannot be vertical, nor can it be broken. It needs to read: VURO or Vuro. Thanks

Target Market(s)

American adults male and female.

Colors
abd036
33a6d7
33b8a4
ffcf3e

Requirements
Must have
• The mandatory information as shown on old labels. The word VURO should be very prominent.
Nice to have
• The uploaded photo of a competitor's prosecco shows a label we really like... if you could play around with this shape and style we'd be very happy.
Should not have
• No grape images, no wine glass images, no images of babies or children.

```html
<!DOCTYPE html>
<html lang="en">
<head>
<meta charset="utf-8">
<title>Vuro Prosecco – Wine Label</title>
<link rel="stylesheet" href="https://fonts.googleapis.com/css2?family=Great+Vibes&family=Cormorant+Garamond:wght@400;500;600&display=swap">
<style>
  :root {
    --backdrop: #e6e6e6;
    --label-black: #0e0e0f;
    --gold: #d9a634;
    --gold-light: #f2cf6a;
    --gold-deep: #b07e1c;
    --ink-soft: #cfcfcf;
  }
  * { margin: 0; padding: 0; box-sizing: border-box; }
  html, body {
    width: 1200px;
    height: 900px;
    overflow: hidden;
    background: var(--backdrop);
  }
  .canvas {
    position: relative;
    width: 1200px;
    height: 900px;
    background: var(--backdrop);
  }
  .label {
    position: absolute;
    left: 258px;
    top: 36px;
    width: 684px;
    height: 828px;
  }
  .label__shape {
    position: absolute;
    inset: 0;
    width: 684px;
    height: 828px;
  }
  .gold-stop-deep { stop-color: var(--gold-deep); }
  .gold-stop-light { stop-color: var(--gold-light); }
  .gold-stop-mid { stop-color: var(--gold); }
  .label__text {
    position: absolute;
    left: 0;
    width: 100%;
    text-align: center;
    line-height: 1;
  }
  .brand-name {
    top: 178px;
    font-family: "Great Vibes", cursive;
    font-weight: 400;
    font-size: 215px;
    color: var(--gold);
  }
  .wine-type {
    top: 452px;
    font-family: "Cormorant Garamond", serif;
    font-weight: 500;
    font-size: 54px;
    letter-spacing: 6px;
    text-transform: uppercase;
    color: var(--gold);
  }
  .region {
    top: 586px;
    font-family: "Cormorant Garamond", serif;
    font-size: 26px;
    color: var(--ink-soft);
  }
  .designation {
    top: 622px;
    font-family: "Cormorant Garamond", serif;
    font-size: 15px;
    color: var(--ink-soft);
  }
  .style-note {
    top: 668px;
    font-family: "Cormorant Garamond", serif;
    font-size: 21px;
    letter-spacing: 2px;
    color: var(--ink-soft);
  }
  .volume {
    top: 740px;
    font-family: "Cormorant Garamond", serif;
    font-size: 22px;
    color: var(--ink-soft);
  }
</style>
</head>
<body>
<main class="canvas">
  <section class="label">
    <svg class="label__shape" viewBox="0 0 285 345" preserveAspectRatio="none" aria-hidden="true">
      <defs>
        <linearGradient id="goldFoil" gradientUnits="userSpaceOnUse" x1="0" y1="0" x2="285" y2="0">
          <stop offset="0" class="gold-stop-deep"/>
          <stop offset="0.35" class="gold-stop-light"/>
          <stop offset="0.65" class="gold-stop-mid"/>
          <stop offset="1" class="gold-stop-deep"/>
        </linearGradient>
      </defs>
      <path class="label__body" fill="#0e0e0f"
        d="M0,52 L18,52 Q24,52 26,46 L30,38 Q32,34 38,34 L88,34 Q92,34 94,30 Q100,14 118,8 Q142.5,2 167,8 Q185,14 191,30 Q193,34 197,34 L247,34 Q253,34 255,38 L259,46 Q261,52 267,52 L285,52 L285,345 L0,345 Z"/>
      <path class="label__crest-line" fill="none" stroke="url(#goldFoil)" stroke-width="2.4"
        d="M0,53 L18,53 Q24,53 26,47 L30,39 Q32,35 38,35 L88,35 Q92,35 94,31 Q100,15 118,9 Q142.5,3 167,9 Q185,15 191,31 Q193,35 197,35 L247,35 Q253,35 255,39 L259,47 Q261,53 267,53 L285,53"/>
      <rect class="label__rule" x="50" y="179.6" width="185" height="0.8" fill="url(#goldFoil)"/>
      <rect class="label__rule" x="50" y="219.6" width="185" height="0.8" fill="url(#goldFoil)"/>
      <rect class="label__base-band" x="6" y="325" width="273" height="2.2" fill="url(#goldFoil)"/>
    </svg>

    <h1 class="label__text brand-name">Vuro</h1>
    <p class="label__text wine-type">Prosecco</p>
    <p class="label__text region">Veneto</p>
    <p class="label__text designation">Indicazione Geografica Tipica</p>
    <p class="label__text style-note">FRIZZANTE</p>
    <p class="label__text volume">750 ml</p>
  </section>
</main>
</body>
</html>
```